TK Business Card

Design a vertical orientation business card with approved logo and fonts (Jubilee Lines and Aviano). Use metallic gold and black, embossing parts of the logo.
Perhaps color back of card black?
Address:
1187 Holloway Crescent
Level 2
West Palm Beach FL 33872

Delphine Marsh
Managing Partner

```html
<!DOCTYPE html>
<html lang="en">
<head>
<meta charset="utf-8">
<title>TK Business Card</title>
<link rel="stylesheet" href="https://fonts.googleapis.com/css2?family=Cinzel:wght@400;700&family=Source+Sans+3:wght@400&display=swap">
<style>
  :root {
    --gold-light: #fbe7a1;
    --gold: #d9ad3c;
    --gold-deep: #a77c1f;
    --gold-metal: linear-gradient(135deg, var(--gold-deep) 0%, var(--gold) 25%, var(--gold-light) 50%, var(--gold) 72%, var(--gold-deep) 100%);
    --ink: #1e1e1e;
    --paper: #ffffff;
    --backdrop: #e9e7e3;
    --edge: #3a3a3a;
  }
  * { margin: 0; padding: 0; box-sizing: border-box; }
  html, body { width: 1200px; height: 758px; overflow: hidden; background: var(--backdrop); }
  .canvas { position: relative; width: 1200px; height: 758px; }

  .card {
    position: absolute; top: 90px;
    width: 330px; height: 578px;
    background: var(--paper);
    border: 1px solid var(--edge);
    overflow: hidden;
  }
  .card--front { left: 52px; }
  .card--back  { left: 434px; }
  .card--blank { left: 816px; }

  .brand-mark {
    position: absolute; left: 0; width: 100%;
    text-align: center;
    font-family: "Cinzel", serif; font-weight: 700;
    color: var(--ink);
  }
  .card--front .brand-mark { top: 46px; font-size: 72px; line-height: 84px; }
  .card--back .brand-mark { top: 170px; font-size: 150px; line-height: 170px; }

  .company {
    position: absolute; left: 0; width: 100%; top: 150px;
    text-align: center;
    font-family: "Cinzel", serif; color: var(--ink);
  }
  .company__name { font-weight: 700; font-size: 20px; letter-spacing: 2px; line-height: 26px; }
  .company__tag { font-size: 15px; letter-spacing: 1.5px; line-height: 22px; }

  .person {
    position: absolute; left: 0; width: 100%; top: 238px;
    text-align: center; font-family: "Cinzel", serif; color: var(--ink);
  }
  .person__name { font-weight: 700; font-size: 17px; letter-spacing: 1.5px; line-height: 24px; }
  .person__role { font-weight: 700; font-size: 11px; letter-spacing: 1.5px; line-height: 20px; }

  .divider {
    position: absolute; left: 135px; top: 302px;
    width: 60px; height: 3px; background: var(--gold-metal);
  }

  .contact {
    position: absolute; left: 0; width: 100%; top: 322px;
    font-family: "Source Sans 3", sans-serif; font-size: 16px;
    color: var(--ink); line-height: 26px; text-align: center;
  }
  .contact__line { display: flex; align-items: center; justify-content: center; gap: 6px; }
  .contact__address { margin-top: 8px; line-height: 23px; }

  .band-gold {
    position: absolute; left: 0; bottom: 0;
    width: 150px; height: 12px; background: var(--gold-metal);
  }
  .band-ink {
    position: absolute; right: 0; bottom: 0; width: 222px; height: 36px;
    background: var(--ink);
    clip-path: polygon(24px 0, 100% 0, 100% 100%, 0 100%);
  }
  .web {
    font-family: "Source Sans 3", sans-serif; font-size: 15px;
    letter-spacing: 2px; white-space: nowrap;
  }
  .band-ink .web {
    position: absolute; left: 24px; right: 0; top: 8px;
    text-align: center; color: var(--paper);
  }
  .card--back .web {
    position: absolute; left: 0; width: 100%; top: 500px;
    text-align: center; color: var(--ink);
  }
</style>
</head>
<body>
<main class="canvas">

  <section class="card card--front">
    <div class="brand-mark">TK</div>
    <div class="company">
      <div class="company__name">TIDE KEEL</div>
      <div class="company__tag">Design Studio</div>
    </div>

    <div class="person">
      <div class="person__name">DELPHINE MARSH</div>
      <div class="person__role">MANAGING PARTNER</div>
    </div>

    <div class="divider"></div>

    <div class="contact">
      <div class="contact__line">
        <svg width="9" height="14" viewBox="0 0 9 14" aria-hidden="true"><rect x="0.5" y="2" width="8" height="11.5" rx="1.5" fill="var(--ink)"/><rect x="2" y="0" width="1.6" height="3" fill="var(--ink)"/><rect x="2" y="4" width="5" height="3.5" fill="#fff"/></svg>
        012-555-0187
      </div>
      <div class="contact__line">
        <svg width="16" height="16" viewBox="0 0 16 16" aria-hidden="true"><circle cx="8" cy="8" r="7" fill="none" stroke="var(--ink)" stroke-width="1.8"/><path d="M5.5 4.5c-.8 2.6.9 5.9 4 7l1.2-1.7-1.8-1.1-.8.7c-1-.6-1.7-1.6-2-2.7l.9-.6-.6-2z" fill="var(--ink)"/></svg>
        012-555-0187
      </div>
      <div class="contact__line">
        <svg width="17" height="15" viewBox="0 0 17 15" aria-hidden="true"><path d="M1 6l7.5-5 7.5 5v8H1z" fill="var(--ink)"/><path d="M3.5 6.5h10L8.5 10z" fill="#fff"/></svg>
        info@tidekeel.com
      </div>
      <div class="contact__address">
        1187 Holloway Crescent, Level 2<br>
        West Palm Beach FL 33872
      </div>
    </div>

    <div class="band-gold"></div>
    <div class="band-ink"><div class="web">www.tidekeel.com</div></div>
  </section>

  <section class="card card--back">
    <div class="brand-mark">TK</div>
    <div class="web">www.tidekeel.com</div>
  </section>

  <section class="card card--blank"></section>

</main>
</body>
</html>
```